Brisk Hollow Builders Needs A Flyer

We need a flyer for our newest product "The Cedarlane Garden Workroom"

Here is some copy for the flyer:

1. More and more people everyday are working from home and finding it difficult to disconnect from home activities in order to focus on their work. They are also finding it very expensive to add on to their existing house for a quiet place. Our archatectually stunning, Cedarlane Garden Workroom is the answer. The office studio measures 16' wide and 10' deep. 160 Square feet of space.

Perfect for dozens of purposes. Home office, design studio, artist studio, home school office, reading room, craft studio, drafting room.

Features include:

- Steel Framing. 40-60% lighter then wood, higher strength to weight ratio, resistant to mold and fire and steel is the most recycled material on earth!
- Spray foam insulation. Cool in the summer and warm in the winter.
- HVAC Mini Split with wireless remote control and thermostat.
- 100% Off grid with enough solar and battery storage to run your entire office. No need to pay for an expensive electric installation.
- Flush fitting floor outlets to reduce wires.
- TV mount (Optional with pre-wired electric, HDMI, digital audio & Cat 6)
- Windows are tempered glass custom made by Morvik Glazing.
- Solar qualifies for a 26% tax credit. This is not a write-off rather it is a direct reduction on your tax obligation.
- Thousands of dollars less than adding onto your home.
- Custom color, siding, features available.

This beautiful back yard office is delivered 100% assembled and ready to enjoy on the day of delivery.

We ship nationwide from our factory in South Carolina. Give us a call anytime to speak to a designer and start your dream office today!

555-318-4027
info@BriskHollowBuilders.example

```html
<!DOCTYPE html>
<html lang="en">
<head>
<meta charset="utf-8">
<title>Brisk Hollow Builders – Cedarlane Garden Workroom</title>
<link href="https://fonts.googleapis.com/css2?family=Nunito+Sans:wght@400;600;700;800&family=Roboto:wght@400;500&display=swap" rel="stylesheet">
<style>
  :root{
    --forest-dark:#17351c;
    --forest:#1f5a2b;
    --amber:#e8a32e;
    --leaf:#3d9b3f;
    --ink:#1c1c1c;
    --paper:#ffffff;
    --mist:#f1f1f3;
  }
  *{margin:0;padding:0;box-sizing:border-box}
  html,body{width:1025px;height:1200px;overflow:hidden;background:var(--paper)}
  .flyer{position:relative;width:1025px;height:1200px;background:var(--paper);font-family:"Roboto",sans-serif;color:var(--ink)}

  .intro-band{position:absolute;left:0;top:0;width:1025px;height:160px;background:var(--forest-dark)}
  .intro-text{position:absolute;left:40px;top:16px;width:942px;color:#fff;font-size:16px;line-height:20px;text-align:justify}

  .purpose-band{position:absolute;left:0;top:118px;width:1025px;height:209px}
  .purpose-title{position:absolute;left:57px;top:128px;font-family:"Nunito Sans",sans-serif;font-weight:700;font-size:24px;line-height:30px;color:#fff}
  .purpose-title::after{content:"";position:absolute;left:50%;bottom:-5px;width:74px;margin-left:-37px;height:3px;background:var(--amber)}
  .purpose-frame{position:absolute;left:26px;top:201px;width:972px;height:106px;border:3px solid var(--amber);border-radius:18px;border-top-color:transparent}
  .purpose-list{position:absolute;left:44px;top:176px;width:940px;display:flex;justify-content:space-between;list-style:none}
  .purpose{width:130px;text-align:center;font-family:"Nunito Sans",sans-serif;font-weight:800;font-size:14.5px;line-height:17px;color:var(--amber)}
  .purpose-icon{display:block;margin:0 auto 8px;width:74px;height:74px;border:2px solid #fff;border-radius:18px;background:var(--forest)}
  .purpose-icon svg{display:block;width:100%;height:100%}

  .right-mist{position:absolute;left:681px;top:327px;width:344px;height:418px;background:var(--mist)}
  .features-band{position:absolute;left:0;top:327px;width:730px;height:62px}
  .features-title{position:absolute;left:40px;top:345px;font-family:"Nunito Sans",sans-serif;font-weight:800;font-size:19.5px;line-height:26px;color:var(--forest-dark);letter-spacing:.2px}

  .feature-list{position:absolute;left:32px;top:430px;width:586px;list-style:none}
  .feature{position:relative;padding-left:48px;font-size:18px;line-height:22px;text-align:justify;margin-bottom:22px}
  .feature .tick{position:absolute;left:0;top:-1px;width:25px;height:25px}

  .photo{position:absolute;border-radius:2px}
  .product-1{left:722px;top:353px;width:222px;height:116px;background:linear-gradient(180deg,#3b3f42 0 14%,#cfd2d0 14% 100%)}
  .product-2{left:801px;top:480px;width:201px;height:106px;background:linear-gradient(180deg,#3b3f42 0 12%,#d8d6cf 12% 100%)}
  .product-3{left:708px;top:599px;width:222px;height:111px;background:linear-gradient(180deg,#35393c 0 16%,#d4d2cb 16% 100%)}

  .note{position:absolute;left:665px;width:360px;color:#fff;font-size:15.5px;line-height:20px;text-align:justify;padding:14px 20px}
  .note-delivery{top:745px;height:92px;background:var(--forest)}
  .note-shipping{top:837px;height:108px;background:var(--forest-dark);padding-top:16px}

  .brand-band{position:absolute;left:700px;top:960px;width:290px;height:150px;border-radius:8px;background:linear-gradient(135deg,#e3f0df,#fbeed3)}
  .brand{position:absolute;left:665px;top:1080px;width:360px;text-align:center;white-space:nowrap}
  .brand-mark{display:inline-block;width:18px;height:18px;border-radius:50%;background:var(--leaf);vertical-align:middle;margin-right:8px}
  .brand-name{font-family:"Nunito Sans",sans-serif;font-weight:800;font-size:26px;line-height:32px;color:var(--amber);vertical-align:middle}
  .brand-phone{position:absolute;left:665px;top:1120px;width:360px;text-align:center;font-family:"Nunito Sans",sans-serif;font-weight:800;font-size:36px;line-height:44px;color:var(--leaf)}
  .brand-email{position:absolute;left:665px;top:1164px;width:360px;text-align:center;font-size:17px;line-height:22px;color:var(--amber)}

  .gallery-1{left:0;top:1068px;width:210px;height:106px;background:linear-gradient(180deg,#7fa6c9 0 35%,#4d6b3a 35% 100%)}
  .gallery-2{left:215px;top:1068px;width:210px;height:106px;background:linear-gradient(180deg,#f2f2f2,#cfcfcf)}
  .gallery-3{left:430px;top:1068px;width:212px;height:106px;background:linear-gradient(180deg,#8fb0cf 0 35%,#5b7446 35% 100%)}
</style>
</head>
<body>
<main class="flyer">
  <div class="intro-band"></div>
  <p class="intro-text">More and more people everyday are working from home and finding it difficult to disconnect from home activities in order to focus on their work. They are also finding it very expensive to add on to their existing house for a quiet place. Our archatectually stunning, Cedarlane Garden Workroom is the answer. The office studio measures 16' wide and 10' deep. 160 Square feet of space.</p>

  <svg class="purpose-band" viewBox="0 0 1025 209" preserveAspectRatio="none" aria-hidden="true">
    <path d="M0 209 V60 Q0 0 60 0 H470 L510 40 H1025 V209 Z" fill="var(--forest)"/>
  </svg>
  <h2 class="purpose-title">Perfect For Dozens Of Purposes</h2>
  <div class="purpose-frame"></div>
  <ul class="purpose-list">
    <li class="purpose"><span class="purpose-icon"><svg viewBox="0 0 84 84" fill="none" stroke="#fff" stroke-width="2.5" stroke-linejoin="round"><path d="M20 42 L42 22 L64 42"/><path d="M26 38 V62 H58 V38"/><rect x="34" y="46" width="16" height="10"/></svg></span>HOME OFFICE</li>
    <li class="purpose"><span class="purpose-icon"><svg viewBox="0 0 84 84" fill="none" stroke="#fff" stroke-width="2.5" stroke-linejoin="round"><rect x="20" y="24" width="44" height="36"/><path d="M24 56 L36 42 L46 52 L52 46 L60 56"/><circle cx="52" cy="34" r="4"/></svg></span>DESIGN STUDIO</li>
    <li class="purpose"><span class="purpose-icon"><svg viewBox="0 0 84 84" fill="none" stroke="#fff" stroke-width="2.5"><path d="M42 22 C26 22 20 34 22 46 C24 58 36 62 42 56 C46 52 50 58 56 56 C64 52 64 38 58 30 C54 24 48 22 42 22 Z"/><circle cx="34" cy="36" r="3"/><circle cx="46" cy="32" r="3"/><circle cx="54" cy="42" r="3"/></svg></span>ARTIST STUDIO</li>
    <li class="purpose"><span class="purpose-icon"><svg viewBox="0 0 84 84" fill="none" stroke="#fff" stroke-width="2.5" stroke-linejoin="round"><path d="M18 44 L42 24 L66 44"/><path d="M24 40 V62 H60 V40"/><path d="M36 62 V50 H48 V62"/></svg></span>HOME SCHOOL OFFICE</li>
    <li class="purpose"><span class="purpose-icon"><svg viewBox="0 0 84 84" fill="none" stroke="#fff" stroke-width="2.5" stroke-linejoin="round"><path d="M42 30 C34 26 26 26 20 28 V60 C26 58 34 58 42 62 C50 58 58 58 64 60 V28 C58 26 50 26 42 30 Z"/><path d="M42 30 V62"/></svg></span>READING ROOM</li>
    <li class="purpose"><span class="purpose-icon"><svg viewBox="0 0 84 84" fill="none" stroke="#fff" stroke-width="2.5" stroke-linejoin="round"><rect x="22" y="30" width="40" height="30"/><path d="M34 30 L42 20 L50 30"/><path d="M30 40 H54 M30 48 H54"/></svg></span>CRAFT STUDIO</li>
    <li class="purpose"><span class="purpose-icon"><svg viewBox="0 0 84 84" fill="none" stroke="#fff" stroke-width="2.5" stroke-linejoin="round"><rect x="20" y="22" width="44" height="32"/><path d="M42 30 L50 35 V44 L42 49 L34 44 V35 Z"/><path d="M28 62 H58"/></svg></span>DRAFTING ROOM</li>
  </ul>

  <div class="right-mist"></div>
  <svg class="features-band" viewBox="0 0 730 62" preserveAspectRatio="none" aria-hidden="true">
    <path d="M0 0 H730 L668 62 H0 Z" fill="var(--amber)"/>
  </svg>
  <h2 class="features-title">FEATURES INCLUDE</h2>

  <ul class="feature-list">
    <li class="feature"><svg class="tick" viewBox="0 0 26 26"><rect x="1.5" y="1.5" width="23" height="23" rx="5" fill="#fff" stroke="var(--amber)" stroke-width="2.5"/><path d="M7 13.5 L11 17.5 L19 8.5" fill="none" stroke="var(--forest)" stroke-width="3" stroke-linecap="round" stroke-linejoin="round"/></svg>Steel Framing. 40-60% lighter then wood, higher strength to weight ratio, resistant to mold and fire and steel is the most recycled material on earth!</li>
    <li class="feature"><svg class="tick" viewBox="0 0 26 26"><rect x="1.5" y="1.5" width="23" height="23" rx="5" fill="#fff" stroke="var(--amber)" stroke-width="2.5"/><path d="M7 13.5 L11 17.5 L19 8.5" fill="none" stroke="var(--forest)" stroke-width="3" stroke-linecap="round" stroke-linejoin="round"/></svg>Spray foam insulation. Cool in the summer and warm in the winter.</li>
    <li class="feature"><svg class="tick" viewBox="0 0 26 26"><rect x="1.5" y="1.5" width="23" height="23" rx="5" fill="#fff" stroke="var(--amber)" stroke-width="2.5"/><path d="M7 13.5 L11 17.5 L19 8.5" fill="none" stroke="var(--forest)" stroke-width="3" stroke-linecap="round" stroke-linejoin="round"/></svg>HVAC Mini Split with wireless remote control and thermostat.</li>
    <li class="feature"><svg class="tick" viewBox="0 0 26 26"><rect x="1.5" y="1.5" width="23" height="23" rx="5" fill="#fff" stroke="var(--amber)" stroke-width="2.5"/><path d="M7 13.5 L11 17.5 L19 8.5" fill="none" stroke="var(--forest)" stroke-width="3" stroke-linecap="round" stroke-linejoin="round"/></svg>100% Off grid with enough solar and battery storage to run your entire office. No need to pay for an expensive electric installation.</li>
    <li class="feature"><svg class="tick" viewBox="0 0 26 26"><rect x="1.5" y="1.5" width="23" height="23" rx="5" fill="#fff" stroke="var(--amber)" stroke-width="2.5"/><path d="M7 13.5 L11 17.5 L19 8.5" fill="none" stroke="var(--forest)" stroke-width="3" stroke-linecap="round" stroke-linejoin="round"/></svg>Flush fitting floor outlets to reduce wires.</li>
    <li class="feature"><svg class="tick" viewBox="0 0 26 26"><rect x="1.5" y="1.5" width="23" height="23" rx="5" fill="#fff" stroke="var(--amber)" stroke-width="2.5"/><path d="M7 13.5 L11 17.5 L19 8.5" fill="none" stroke="var(--forest)" stroke-width="3" stroke-linecap="round" stroke-linejoin="round"/></svg>TV mount (Optional with pre-wired electric, HDMI, digital audio &amp; Cat 6)</li>
    <li class="feature"><svg class="tick" viewBox="0 0 26 26"><rect x="1.5" y="1.5" width="23" height="23" rx="5" fill="#fff" stroke="var(--amber)" stroke-width="2.5"/><path d="M7 13.5 L11 17.5 L19 8.5" fill="none" stroke="var(--forest)" stroke-width="3" stroke-linecap="round" stroke-linejoin="round"/></svg>Windows are tempered glass custom made by Morvik Glazing.</li>
    <li class="feature"><svg class="tick" viewBox="0 0 26 26"><rect x="1.5" y="1.5" width="23" height="23" rx="5" fill="#fff" stroke="var(--amber)" stroke-width="2.5"/><path d="M7 13.5 L11 17.5 L19 8.5" fill="none" stroke="var(--forest)" stroke-width="3" stroke-linecap="round" stroke-linejoin="round"/></svg>Solar qualifies for a 26% tax credit. This is not a write-off rather it is a direct reduction on your tax obligation.</li>
    <li class="feature"><svg class="tick" viewBox="0 0 26 26"><rect x="1.5" y="1.5" width="23" height="23" rx="5" fill="#fff" stroke="var(--amber)" stroke-width="2.5"/><path d="M7 13.5 L11 17.5 L19 8.5" fill="none" stroke="var(--forest)" stroke-width="3" stroke-linecap="round" stroke-linejoin="round"/></svg>Thousands of dollars less than adding onto your home.</li>
  </ul>

  <div class="photo product-1" role="img" aria-label="Garden workroom with dark siding and glass front, angled view"></div>
  <div class="photo product-2" role="img" aria-label="Garden workroom front view showing glazed wall and furnished interior"></div>
  <div class="photo product-3" role="img" aria-label="Garden workroom seen from the other side with sloped roof"></div>

  <p class="note note-delivery">This beautiful back yard office is delivered 100% assembled and ready to enjoy on the day of delivery.</p>
  <p class="note note-shipping">We ship nationwide from our factory in South Carolina. Give us a call anytime to speak to a designer and start your dream office today!</p>

  <div class="brand-band" role="img" aria-label="Soft green and amber backdrop behind the company name"></div>
  <div class="brand"><span class="brand-mark"></span><span class="brand-name">Brisk Hollow Builders</span></div>
  <div class="brand-phone">555-318-4027</div>
  <div class="brand-email">info@BriskHollowBuilders.example</div>

  <div class="photo gallery-1" role="img" aria-label="Workroom placed in a leafy garden at dusk"></div>
  <div class="photo gallery-2" role="img" aria-label="Steel frame of the workroom before cladding"></div>
  <div class="photo gallery-3" role="img" aria-label="Rear of the workroom with solar panels on the roof"></div>
</main>
</body>
</html>
```